Portugal:the best eco sun-dried tomato in the world needs a packaging design

We produce the best sun-dried tomatoes in the world...we know that, even that competition doesn´t exist...yet!
We are a "solar farm" in Portugal, reducing carbon footprint producing beautiful and healthy local food, with mules...the traditional way in a new way. Our tomatoes are hand-picked and sun dried, in a very "slow food" way.
The costumers for our product -we are a small farm - can only be good foodstores and airports, we'd love to export the best of Portugal elsewhere. In a glass jar of c. 250 ml, with a nice top and a nice logo+description...one that stands out of the others and conveys our eco, local, solar message.
Oh, and I forgot...our sun-dried tomatoes are packed with our beautiful olive oil..and yes, that olive oil has already won the best olive oil in the world! For sure!
I'll send photos for the interested, you'll love it; and the best olive oil and sun-dried tomatoes in the world for the winner!

Target Market(s)

nice foodstores
foodies
airport stores

Industry/Entity Type

Food Store

Font styles to use
Decorative
Script

Requirements
Must have
• Portugal
• Sun dried tomatoes
• Best olive oil in the world
• Traditional methods
• Sustainable farming
Nice to have
• a photo of our mules working...sent to interested designers

```html
<!DOCTYPE html>
<html lang="en">
<head>
<meta charset="utf-8">
<title>Sun Dried Tomatoes – Jar Label</title>
<link rel="stylesheet" href="https://fonts.googleapis.com/css2?family=Montserrat:wght@400;500&family=Alfa+Slab+One&family=Playfair+Display:wght@600&family=Caveat:wght@700&display=swap">
<style>
  :root {
    --tomato-dark: #3a0503;
    --tomato-mid: #8c1205;
    --tomato-bright: #d42a0c;
    --label-red: #a8121a;
    --label-red-deep: #8d0e14;
    --label-green: #1b6b34;
    --label-white: #ffffff;
    --label-silver: #cfcfcf;
    --sun-gold: #a8977a;
    --sun-gold-soft: #e4dccd;
  }
  * { margin: 0; padding: 0; box-sizing: border-box; }
  html, body {
    width: 1200px; height: 1000px; overflow: hidden;
    background: var(--tomato-dark);
  }
  .canvas { position: relative; width: 1200px; height: 1000px; overflow: hidden; }
  .backdrop {
    position: absolute; inset: 0;
    background:
      radial-gradient(ellipse at 20% 15%, var(--tomato-bright) 0%, transparent 45%),
      radial-gradient(ellipse at 85% 80%, var(--tomato-bright) 0%, transparent 40%),
      radial-gradient(ellipse at 60% 40%, var(--tomato-mid) 0%, var(--tomato-dark) 75%);
  }
  .label { position: absolute; left: 0; top: 0; }
  .arc-title { font-family: "Montserrat", sans-serif; font-weight: 400; font-size: 68px; fill: var(--label-white); }
  .arc-claims { font-family: "Playfair Display", serif; font-weight: 600; font-size: 26px; fill: var(--label-white); }
  .product-kind { font-family: "Montserrat", sans-serif; font-weight: 500; font-size: 42px; fill: var(--label-red); }
  .product-name {
    font-family: "Alfa Slab One", serif; font-size: 84px;
    fill: var(--label-red); stroke: var(--label-red-deep); stroke-width: 1;
  }
  .product-name-inline { font-family: "Alfa Slab One", serif; font-size: 84px; fill: none; stroke: var(--label-white); stroke-width: 2; }
  .tagline { font-family: "Caveat", cursive; font-weight: 700; font-size: 30px; fill: var(--sun-gold); }
  .volume { font-family: "Playfair Display", serif; font-weight: 600; fill: var(--label-white); }
  .ornament-area { fill: var(--sun-gold-soft); }
</style>
</head>
<body>
<div class="canvas">
  <div class="backdrop" role="img" aria-label="Close-up photograph of sun-dried tomatoes"></div>

  <svg class="label" width="1200" height="1000" viewBox="0 0 1200 1000" xmlns="http://www.w3.org/2000/svg">
    <defs>
      <radialGradient id="silver-rim" cx="50%" cy="42%" r="55%">
        <stop offset="72%" stop-color="var(--label-white)"/>
        <stop offset="100%" stop-color="var(--label-silver)"/>
      </radialGradient>
      <clipPath id="label-face"><circle cx="600" cy="505" r="376"/></clipPath>
      <path id="arc-top" d="M 310 505 A 290 290 0 0 1 890 505"/>
      <path id="arc-bottom" d="M 265 505 A 335 335 0 0 0 935 505"/>
    </defs>

    <!-- outer rim -->
    <circle cx="600" cy="505" r="412" fill="url(#silver-rim)"/>

    <!-- red face -->
    <circle cx="600" cy="505" r="376" fill="var(--label-red)"/>

    <!-- green ring and white centre -->
    <circle cx="600" cy="505" r="268" fill="var(--label-green)"/>
    <circle cx="600" cy="505" r="252" fill="var(--label-white)"/>

    <!-- middle white band -->
    <rect x="200" y="400" width="800" height="178" fill="var(--label-white)" clip-path="url(#label-face)"/>

    <!-- arc texts -->
    <text class="arc-title"><textPath href="#arc-top" startOffset="50%" text-anchor="middle" textLength="660" lengthAdjust="spacing">PORTUGAL</textPath></text>
    <text class="arc-claims"><textPath href="#arc-bottom" startOffset="50%" text-anchor="middle" textLength="800" lengthAdjust="spacing">TRADITIONAL METHODS • SUSTAINABLE FARMING</textPath></text>

    <!-- sun ornament area -->
    <rect class="ornament-area" x="505" y="300" width="220" height="90" rx="10" role="img" aria-label="Rising sun ray ornament"/>

    <!-- product naming -->
    <text class="product-kind" x="600" y="446" text-anchor="middle" textLength="344" lengthAdjust="spacingAndGlyphs">SUN DRIED</text>
    <text class="product-name" x="600" y="534" text-anchor="middle" textLength="720" lengthAdjust="spacingAndGlyphs">TOMATOES</text>
    <text class="product-name-inline" x="605" y="529" text-anchor="middle" textLength="720" lengthAdjust="spacingAndGlyphs">TOMATOES</text>
    <text class="tagline" x="600" y="582" text-anchor="middle" textLength="390" lengthAdjust="spacingAndGlyphs">With the best olive oil in the world!</text>

    <!-- heraldic emblem area -->
    <rect class="ornament-area" x="450" y="605" width="300" height="85" rx="10" role="img" aria-label="Heraldic shield emblem with flourishes"/>

    <!-- volume badge -->
    <circle cx="600" cy="748" r="52" fill="var(--label-red)"/>
    <text class="volume" x="600" y="754" text-anchor="middle" font-size="28" letter-spacing="3">250</text>
    <text class="volume" x="600" y="787" text-anchor="middle" font-size="18" letter-spacing="2">ML</text>
  </svg>
</div>
</body>
</html>
```